Looking for a contemporary business card design with our logo

would like to consider a embossing look although I'm not married to the idea. We are a custom jeweler that needs a look that represents old world craftsmanship with a modern twist that's why we went with a more modern shield type of logo that can be stamped inside our rings.
It could be two sided or one we are more after a look the pops and is trendy and creative. (WE ARE NOT LOOKING FOR A COOKIE CUTTER LAYOUT)
We have attached the image and will be using the logo with kestrel forge wording in the format that it's in unless you see a better way of doing it.
If the logo needs a twist we are O.K. with suggestions as well.
This card should scream "Quality" from a high end studio.
Kestrel Forge
4189 Malbrook Rd. Unit C-7
Larkfield, NV 89614
www.kestrelforge.example
mo@kestrelforge.example
Should speak quality craftsmanship

```html
<!DOCTYPE html>
<html lang="en">
<head>
<meta charset="utf-8">
<title>Kestrel Forge – Business Card</title>
<link rel="stylesheet" href="https://fonts.googleapis.com/css2?family=Open+Sans:wght@400;600&display=swap">
<style>
  :root {
    --stage: #2a2624;
    --card-black: #1b1b1c;
    --card-black-edge: #111112;
    --silver-light: #eeeeef;
    --silver-mid: #b9babc;
    --silver-dark: #7d7e80;
    --text-silver: #d6d6d8;
    --emboss: #3a3a3c;
  }
  * { box-sizing: border-box; margin: 0; padding: 0; }
  html, body { width: 1200px; height: 680px; overflow: hidden; }
  body {
    background: var(--stage);
    font-family: "Open Sans", Arial, sans-serif;
    position: relative;
  }
  .card {
    position: absolute;
    top: 186px;
    width: 540px;
    height: 308px;
    background: linear-gradient(135deg, #232324 0%, var(--card-black) 55%, var(--card-black-edge) 100%);
    border-radius: 4px;
    box-shadow: 0 14px 30px rgba(0,0,0,0.55);
    overflow: hidden;
  }
  .card--back { left: 40px; }
  .card--front { left: 620px; }

  /* Back: embossed name mark */
  .back-mark {
    position: absolute;
    inset: 0;
    display: flex;
    flex-direction: column;
    align-items: center;
    justify-content: center;
    gap: 16px;
  }
  .back-mark__square {
    width: 64px; height: 64px;
    border: 3px solid var(--emboss);
  }
  .back-mark__name {
    font-size: 34px;
    font-weight: 400;
    letter-spacing: 6px;
    text-transform: uppercase;
    white-space: nowrap;
    color: var(--emboss);
  }

  /* Front */
  .silver-band {
    position: absolute;
    left: 38px; top: 0;
    width: 52px; height: 100%;
    background: linear-gradient(90deg, var(--silver-dark) 0%, var(--silver-light) 45%, var(--silver-mid) 100%);
  }
  .silver-band__square {
    position: absolute;
    left: 11px; top: 22px;
    width: 30px; height: 30px;
    border: 2px solid #555658;
  }
  .contact {
    position: absolute;
    left: 104px; top: 148px;
    color: var(--text-silver);
    font-size: 12.5px;
    line-height: 1.45;
    white-space: nowrap;
  }
  .contact__company { font-size: 17px; margin-bottom: 2px; }
  .contact__row { display: flex; align-items: center; gap: 6px; }
  .contact__row svg { width: 11px; height: 11px; flex: none; }
  .contact__address { margin-bottom: 2px; }

  .front-mark {
    position: absolute;
    right: 26px; top: 78px;
    width: 236px;
    display: flex;
    flex-direction: column;
    align-items: center;
    gap: 16px;
  }
  .front-mark__square {
    width: 62px; height: 62px;
    border: 3px solid var(--silver-mid);
  }
  .front-mark__name {
    font-size: 22px;
    font-weight: 400;
    letter-spacing: 3px;
    text-transform: uppercase;
    white-space: nowrap;
    color: var(--silver-mid);
    text-align: center;
  }
</style>
</head>
<body>
  <section class="card card--back" aria-label="Card back">
    <div class="back-mark">
      <div class="back-mark__square"></div>
      <div class="back-mark__name">Kestrel Forge</div>
    </div>
  </section>

  <section class="card card--front" aria-label="Card front">
    <div class="silver-band"><div class="silver-band__square"></div></div>

    <div class="contact">
      <div class="contact__company">Kestrel Forge</div>
      <div>4189 Malbrook Rd. Unit C-7</div>
      <div class="contact__address">Larkfield, NV 89614</div>
      <div class="contact__row">
        <svg viewBox="0 0 12 12" aria-hidden="true"><rect x="1" y="2.5" width="10" height="7" fill="none" stroke="#d6d6d8"/><path d="M1 2.5 6 6.5 11 2.5" fill="none" stroke="#d6d6d8"/></svg>
        <span>mo@kestrelforge.example</span>
      </div>
      <div class="contact__row">
        <svg viewBox="0 0 12 12" aria-hidden="true"><rect x="1" y="1.5" width="10" height="7" fill="none" stroke="#d6d6d8"/><path d="M4 10.5h4M6 8.5v2" stroke="#d6d6d8"/></svg>
        <span>www.kestrelforge.example</span>
      </div>
    </div>

    <div class="front-mark">
      <div class="front-mark__square"></div>
      <div class="front-mark__name">Kestrel Forge</div>
    </div>
  </section>
</body>
</html>
```